(new) Verdant Pathway Health Coaching business needs a WordPress theme/website!

Hi! I am launching my health coaching business (7mapleroots Nutrition Coaching) and am need of a site design that I can plug into WordPress. I've attached my logos, social media squares, and one program form template -- I would like the website to reflect and compliment this branding so far (working tagline of "Health is for every body"... though I am open to suggestions). If helpful, my personal IG is @tilvarenq as all photos there are my original work.

The site should include blog, about me, contact me, testimonials, and health history form templates that I can customize if needed. The overall look and feel should me minimalist yet warm and inviting. My offerings will enable the client to consider what truly nourishes their lives in addition to the food on their plate. Thanks in advance!

```html
<!DOCTYPE html>
<html lang="en">
<head>
<meta charset="utf-8">
<title>7mapleroots Nutrition Coaching</title>
<link href="https://fonts.googleapis.com/css2?family=Montserrat:wght@300;400;500;600&display=swap" rel="stylesheet">
<style>
:root{
  --brand:#0b5f9a;
  --ink:#1d1d1d;
  --body:#555;
  --line:#dcdcdc;
  --footer:#2c2c2c;
  --white:#fff;
}
*{box-sizing:border-box;margin:0;padding:0}
html,body{width:1200px;height:4286px;overflow:hidden;background:var(--white)}
body{position:relative;font-family:'Montserrat',sans-serif;color:var(--ink)}
.abs{position:absolute}
a{color:inherit;text-decoration:none}

/* header */
.site-header{left:0;top:0;width:1200px;height:127px;background:var(--white)}
.brand{display:flex;align-items:center;gap:10px;color:var(--brand);font-size:16px;font-weight:500;white-space:nowrap}
.brand-dot{width:14px;height:14px;border-radius:50%;background:var(--brand);flex:none}
.site-header .brand{left:88px;top:52px}
.search{left:535px;top:26px;width:212px;height:28px;border-bottom:1px solid var(--line);font-size:12px;color:#999;letter-spacing:1px;padding:4px 6px}
.search svg{position:absolute;right:6px;top:4px}
.login{left:813px;top:33px;font-size:16px;color:var(--brand);letter-spacing:1px}
.phone{left:925px;top:30px;font-size:19px;color:var(--brand);letter-spacing:1px;display:flex;align-items:center;gap:10px}
.main-nav{left:393px;top:90px;display:flex;gap:29px;font-size:14.5px;letter-spacing:1.2px;color:#444}
.main-nav .active{color:var(--brand)}

/* hero */
.hero{left:0;top:127px;width:1200px;height:590px;background:linear-gradient(180deg,#7c8f5e 0%,#9aaa70 40%,#6f8a3d 75%,#4e6a2a 100%)}
.hero-title{left:0;top:345px;width:1200px;text-align:center;color:var(--white);font-size:51px;font-weight:500;letter-spacing:4px}
.btn{display:inline-flex;align-items:center;justify-content:center;border-radius:30px;font-weight:600}
.hero-btn{left:510px;top:436px;width:180px;height:50px;background:var(--brand);color:var(--white);font-size:16px;letter-spacing:1px}

/* about */
.about-photo{left:156px;top:816px;width:432px;height:432px;border-radius:50%;background:radial-gradient(circle at 50% 45%,#8a8070,#5c6a4e 60%,#3f4a36)}
.about-title{left:634px;top:842px;font-size:46px;font-weight:500}
.about-text{left:634px;top:920px;width:472px;font-size:15px;font-weight:300;line-height:35px;color:var(--body);text-align:justify}
.about-btn{left:634px;top:1160px;width:156px;height:50px;background:var(--brand);color:var(--white);font-size:15px}

/* programs */
.programs{left:0;top:1349px;width:1200px;height:555px;background:var(--brand)}
.section-title{width:1200px;left:0;text-align:center;font-size:46px;font-weight:500}
.programs .section-title{top:88px;color:var(--white)}
.program{top:162px;width:248px;text-align:center;color:var(--white)}
.program-img{height:179px;width:100%}
.program h3{font-size:22px;font-weight:500;margin-top:12px}
.program p{font-size:13.5px;font-weight:300;line-height:24px;margin-top:8px;padding:0 6px}

/* testimonials */
.testi-title{top:1990px}
.testimonial{top:2066px;width:502px;height:306px;background:linear-gradient(135deg,#4a4a4a,#2e2e2e)}
.testimonial .rule{left:38px;top:34px;width:2px;height:176px;background:var(--white)}
.testimonial .quote{left:54px;top:30px}
.testimonial blockquote{left:54px;top:86px;width:420px;color:var(--white);font-size:16px;font-weight:300;line-height:30px}
.testimonial cite{left:54px;top:186px;color:var(--white);font-size:16px;font-weight:600;font-style:normal}
.testimonial .mini-brand{right:10px;top:258px;color:var(--white);font-size:12px;font-weight:500}

/* health history */
.history{left:0;top:2472px;width:1200px;height:389px;background:linear-gradient(180deg,#0d5f98,#0b66a4 55%,#0a5a92)}
.history .section-title{top:88px;color:var(--white)}
.history p{left:150px;top:166px;width:900px;text-align:center;color:var(--white);font-size:14.5px;font-weight:300;line-height:28px}
.history-btn{left:486px;top:239px;width:228px;height:48px;border:2px solid var(--white);color:var(--white);font-size:16px;gap:10px}

/* blog */
.blog-title{top:2947px}
.post{top:3021px;width:320px;height:443px;background:var(--white);box-shadow:0 2px 14px rgba(0,0,0,.12)}
.post-img{height:220px;width:100%}
.post .date{left:12px;top:207px;height:30px;padding:0 16px;background:var(--brand);color:var(--white);font-size:13px;border-radius:16px;display:flex;align-items:center}
.post h3{left:20px;top:252px;font-size:22px;font-weight:500}
.post p{left:20px;top:295px;width:285px;font-size:14.5px;font-weight:300;line-height:27px;color:var(--body)}
.post .more{left:20px;top:401px;font-size:14px;font-weight:600;color:var(--brand)}
.post .arrow{right:20px;top:404px}

/* contact */
.contact-title{top:3550px}
.contact-item{top:3638px;width:320px;text-align:center;font-size:15.5px;line-height:27px;color:#333}
.contact-icon{margin:0 auto 16px;width:86px;height:86px;border:2px solid var(--brand);border-radius:50%;display:flex;align-items:center;justify-content:center}

/* footer */
.site-footer{left:0;top:3883px;width:1200px;height:403px;background:var(--footer);color:var(--white)}
.site-footer .brand{left:90px;top:82px;font-size:15px;color:#3d8cc4}
.site-footer h4{font-size:22px;font-weight:500}
.links-head{left:432px;top:66px}
.link-col{top:120px;font-size:14.5px;line-height:30px;font-weight:300;list-style:none}
.follow-head{left:1002px;top:66px}
.social{left:1002px;top:120px;list-style:none;font-size:14.5px;line-height:30px;font-weight:300}
.social li{display:flex;align-items:center;gap:16px}
.social .dot{width:8px;height:8px;background:var(--white);border-radius:50%}
.copyright{left:0;top:360px;width:1200px;text-align:center;font-size:12.5px;font-weight:300}
</style>
</head>
<body>

<header class="abs site-header">
  <div class="abs brand"><span class="brand-dot"></span>7mapleroots Nutrition Coaching</div>
  <div class="abs search">SEARCH
    <svg width="16" height="16" viewBox="0 0 16 16"><circle cx="6.5" cy="6.5" r="4.5" fill="none" stroke="#777" stroke-width="2"/><line x1="10" y1="10" x2="14" y2="14" stroke="#777" stroke-width="2"/></svg>
  </div>
  <a class="abs login">LOGIN</a>
  <div class="abs phone">
    <svg width="16" height="16" viewBox="0 0 24 24"><path fill="#0b5f9a" d="M6.6 10.8a15 15 0 0 0 6.6 6.6l2.2-2.2a1 1 0 0 1 1-.25 11.4 11.4 0 0 0 3.6.57 1 1 0 0 1 1 1V20a1 1 0 0 1-1 1A17 17 0 0 1 3 4a1 1 0 0 1 1-1h3.5a1 1 0 0 1 1 1c0 1.25.2 2.45.57 3.57a1 1 0 0 1-.25 1z"/></svg>
    (555) 214-7730
  </div>
  <nav class="abs main-nav">
    <a class="active">HOME</a><a>BLOG</a><a>ABOUT ME</a><a>CONTACT ME</a><a>TESTIMONIALS</a><a>HEALTH HISTORY</a>
  </nav>
</header>

<section class="abs hero" role="img" aria-label="Two older adults doing a balance yoga pose outdoors in a sunny park"></section>
<h1 class="abs hero-title">HEALTH IS FOR EVERYBODY</h1>
<a class="abs btn hero-btn">Get a Quote</a>

<div class="abs about-photo" role="img" aria-label="Portrait of the coach hugging a tree outdoors"></div>
<h2 class="abs about-title">About Me</h2>
<p class="abs about-text">Lorem ipsum dolor sit amet, consectetur adipiscing elit, sed do eiusmod tempor incididunt ut labore et dolore magna aliqua. Ut enim ad minim veniam, quis nostrud exercitation ullamco laboris nisi ut aliquip ex ea commodo consequat. Duis aute irure dolor in reprehenderit in voluptate velit esse cillum dolore eu fugiat nulla pariatur.</p>
<a class="abs btn about-btn">Read More</a>

<section class="abs programs">
  <h2 class="abs section-title">Health &amp; Wellness Program</h2>
  <div class="abs program" style="left:88px">
    <div class="program-img" role="img" aria-label="Gym with kettlebells in black and white" style="background:linear-gradient(180deg,#cfcfcf,#777 70%,#333)"></div>
    <h3>Individual Coaching</h3>
    <p>Lorem ipsum dolor sit amet, consectetur adipiscing elit, sed do eiusmod tempor</p>
  </div>
  <div class="abs program" style="left:347px">
    <div class="program-img" role="img" aria-label="Group exercising in a climbing gym" style="background:linear-gradient(180deg,#c9c3bd,#8a7f78 60%,#5b6a80)"></div>
    <h3>Group Coaching</h3>
    <p>Lorem ipsum dolor sit amet, consectetur adipiscing elit, sed do eiusmod tempor</p>
  </div>
  <div class="abs program" style="left:604px">
    <div class="program-img" role="img" aria-label="Fresh vegetable salad with tomatoes" style="background:linear-gradient(135deg,#4f7a2e,#b23a2e 50%,#6a8a3a)"></div>
    <h3>Vegan Retreats</h3>
    <p>Lorem ipsum dolor sit amet, consectetur adipiscing elit, sed do eiusmod tempor</p>
  </div>
  <div class="abs program" style="left:862px">
    <div class="program-img" role="img" aria-label="Healthy salad with sliced meat" style="background:linear-gradient(135deg,#d9c6b8,#b98a80 50%,#6f8a45)"></div>
    <h3>Healthy Diet</h3>
    <p>Lorem ipsum dolor sit amet, consectetur adipiscing elit, sed do eiusmod tempor</p>
  </div>
</section>

<h2 class="abs section-title testi-title">Testimonials</h2>
<article class="abs testimonial" style="left:88px" role="img" aria-label="Client in a coaching session, darkened background">
  <span class="abs rule"></span>
  <svg class="abs quote" width="50" height="36" viewBox="0 0 50 36"><path fill="#fff" d="M0 36V18C0 8 5 2 14 0l2 5c-5 2-7 6-7 11h7v20zM27 36V18c0-10 5-16 14-18l2 5c-5 2-7 6-7 11h7v20z"/></svg>
  <blockquote class="abs">Lorem ipsum dolor sit amet, consectetur adipiscing elit, sed do eiusmod tempor incididunt ut labore et dolore magna aliqua.</blockquote>
  <cite class="abs">-Marisol</cite>
  <span class="abs mini-brand">7mapleroots</span>
</article>
<article class="abs testimonial" style="left:609px" role="img" aria-label="Group yoga class in a bright studio, darkened background">
  <span class="abs rule"></span>
  <svg class="abs quote" width="50" height="36" viewBox="0 0 50 36"><path fill="#fff" d="M0 36V18C0 8 5 2 14 0l2 5c-5 2-7 6-7 11h7v20zM27 36V18c0-10 5-16 14-18l2 5c-5 2-7 6-7 11h7v20z"/></svg>
  <blockquote class="abs">Lorem ipsum dolor sit amet, consectetur adipiscing elit, sed do eiusmod tempor incididunt ut labore et dolore magna aliqua.</blockquote>
  <cite class="abs">-Tobin</cite>
  <span class="abs mini-brand">7mapleroots</span>
</article>

<section class="abs history" role="img" aria-label="Blue-tinted photo of people stretching in a class">
  <h2 class="abs section-title">Health History</h2>
  <p class="abs">Lorem ipsum dolor sit amet, consectetur adipiscing elit, sed do eiusmod tempor incididunt ut labore et dolore magna aliqua. Ut enim ad minim veniam, quis nostrud exercitation ullamco laboris nisi ut aliquip ex ea commodo consequat.</p>
  <a class="abs btn history-btn">
    <svg width="14" height="14" viewBox="0 0 14 14"><path fill="#fff" d="M5 0h4v6h3L7 11 2 6h3zM0 12h14v2H0z"/></svg>
    Download Form
  </a>
</section>

<h2 class="abs section-title blog-title">Latest Blog</h2>
<article class="abs post" style="left:90px">
  <div class="post-img" role="img" aria-label="Colorful roasted vegetable dish" style="background:linear-gradient(135deg,#8a9a3a,#8a2a3a 50%,#c8b070)"></div>
  <span class="abs date">April 22, 2019</span>
  <h3 class="abs">Featured Content</h3>
  <p class="abs">Lorem ipsum dolor sit amet, consectetur adipiscing elit, sed do eiusmod tempor incididunt ut</p>
  <a class="abs more">Read More</a>
  <svg class="abs arrow" width="28" height="10" viewBox="0 0 28 10"><path d="M0 5h26M21 1l5 4-5 4" fill="none" stroke="#0b5f9a" stroke-width="2"/></svg>
</article>
<article class="abs post" style="left:441px">
  <div class="post-img" role="img" aria-label="White blossom flowers close up" style="background:radial-gradient(circle at 50% 60%,#f4eaea,#d8c8c8 60%,#8a7a6a)"></div>
  <span class="abs date">April 22, 2019</span>
  <h3 class="abs">Featured Content</h3>
  <p class="abs">Lorem ipsum dolor sit amet, consectetur adipiscing elit, sed do eiusmod tempor incididunt ut</p>
  <a class="abs more">Read More</a>
  <svg class="abs arrow" width="28" height="10" viewBox="0 0 28 10"><path d="M0 5h26M21 1l5 4-5 4" fill="none" stroke="#0b5f9a" stroke-width="2"/></svg>
</article>
<article class="abs post" style="left:790px">
  <div class="post-img" role="img" aria-label="Flower garden in front of a red barn" style="background:linear-gradient(180deg,#6a8a4a,#4a6a30 50%,#8a6aa0)"></div>
  <span class="abs date">April 22, 2019</span>
  <h3 class="abs">Featured Content</h3>
  <p class="abs">Lorem ipsum dolor sit amet, consectetur adipiscing elit, sed do eiusmod tempor incididunt ut</p>
  <a class="abs more">Read More</a>
  <svg class="abs arrow" width="28" height="10" viewBox="0 0 28 10"><path d="M0 5h26M21 1l5 4-5 4" fill="none" stroke="#0b5f9a" stroke-width="2"/></svg>
</article>

<h2 class="abs section-title contact-title">Contact Me</h2>
<div class="abs contact-item" style="left:115px">
  <div class="contact-icon"><svg width="20" height="20" viewBox="0 0 24 24"><path fill="#0b5f9a" d="M6.6 10.8a15 15 0 0 0 6.6 6.6l2.2-2.2a1 1 0 0 1 1-.25 11.4 11.4 0 0 0 3.6.57 1 1 0 0 1 1 1V20a1 1 0 0 1-1 1A17 17 0 0 1 3 4a1 1 0 0 1 1-1h3.5a1 1 0 0 1 1 1c0 1.25.2 2.45.57 3.57a1 1 0 0 1-.25 1z"/></svg></div>
  Phone<br>(555) 214-7730
</div>
<div class="abs contact-item" style="left:433px">
  <div class="contact-icon"><svg width="16" height="22" viewBox="0 0 16 22"><path fill="#0b5f9a" d="M8 0a8 8 0 0 0-8 8c0 6 8 14 8 14s8-8 8-14a8 8 0 0 0-8-8zm0 11a3 3 0 1 1 0-6 3 3 0 0 1 0 6z"/></svg></div>
  218 Alder Hollow Lane, Brookfield<br>ST 40517
</div>
<div class="abs contact-item" style="left:751px">
  <div class="contact-icon"><svg width="22" height="16" viewBox="0 0 22 16"><rect width="22" height="16" rx="2" fill="#0b5f9a"/><path d="M1 2l10 7 10-7" fill="none" stroke="#fff" stroke-width="1.6"/></svg></div>
  Email<br>hello@maplerootscoach.com
</div>

<footer class="abs site-footer">
  <div class="abs brand"><span class="brand-dot" style="background:#3d8cc4"></span>7mapleroots Nutrition Coaching</div>
  <h4 class="abs links-head">Links</h4>
  <ul class="abs link-col" style="left:432px">
    <li>Home</li><li>Blog</li><li>About Me</li><li>Contact Me</li><li>Testimonials</li><li>Health History</li>
  </ul>
  <ul class="abs link-col" style="left:719px">
    <li>About Us</li><li>Review</li><li>sitemap</li>
  </ul>
  <h4 class="abs follow-head">Follow Us</h4>
  <ul class="abs social">
    <li><span class="dot"></span>Community</li>
    <li><span class="dot"></span>Network</li>
  </ul>
  <p class="abs copyright">Copyright © 2020 The Company Name. All rights reserved.</p>
</footer>

</body>
</html>
```